3 App Screens Designed

I have a laundry app and the developers want 3 images to replace the standard 3 attached.

The images should be custom made with a laundry theme and NOT downloaded from an image site

The app background will be white and the images I need to submit must be 1024 x 1024 with transparent background.

NOTE: I only need the images and not the app face.

Thanks

Colors
0054AA
0677BA
7BADD7
CADEEF
E8F1F8

```html
<!DOCTYPE html>
<html lang="en">
<head>
<meta charset="utf-8">
<title>Laundry App Onboarding Screens</title>
<link rel="stylesheet" href="https://fonts.googleapis.com/css2?family=Poppins:wght@600;700&family=Roboto:wght@400;500&display=swap">
<style>
  :root {
    --navy: #0054AA;
    --blue: #0677BA;
    --sky: #7BADD7;
    --mist: #CADEEF;
    --ice: #E8F1F8;
    --ink: #1B1B1F;
    --grey: #55585E;
    --white: #FFFFFF;
  }
  * { box-sizing: border-box; margin: 0; padding: 0; }
  html, body { width: 1200px; height: 803px; overflow: hidden; }
  body {
    background: var(--white);
    font-family: "Roboto", Arial, sans-serif;
    position: relative;
  }
  .backdrop-wave { position: absolute; top: 0; left: 0; }

  .screen {
    position: absolute;
    top: 142px;
    width: 252px;
    height: 545px;
    background: var(--white);
    border-radius: 26px;
    box-shadow: 0 0 0 10px #EEF0F3, 0 8px 24px rgba(0, 40, 90, 0.18);
    overflow: hidden;
  }
  .screen--date { left: 100px; }
  .screen--pickup { left: 454px; }
  .screen--receive { left: 807px; }

  .status-bar {
    position: absolute; top: 13px; left: 14px; right: 14px;
    display: flex; justify-content: space-between; align-items: center;
    font-size: 9px; font-weight: 500; color: var(--ink);
  }
  .status-icons { display: flex; gap: 3px; align-items: center; }

  .app-header {
    position: absolute; top: 38px; left: 0; right: 0; height: 24px;
    display: flex; align-items: center; justify-content: center;
  }
  .app-header__back { position: absolute; left: 14px; top: 8px; }
  .app-header__title {
    font-weight: 500; font-size: 13.5px; color: var(--ink);
  }
  .app-header__menu {
    position: absolute; right: 14px; top: 1px;
    width: 23px; height: 23px; border-radius: 50%;
    background: #E4E6EA;
    display: flex; align-items: center; justify-content: center;
  }

  .illustration {
    position: absolute; top: 110px; left: 36px; right: 36px; height: 160px;
    border-radius: 6px;
    background: linear-gradient(180deg, var(--white) 0%, var(--ice) 45%, var(--mist) 100%);
  }
  .screen--pickup .illustration {
    background: linear-gradient(180deg, var(--white) 0%, var(--mist) 55%, var(--sky) 100%);
  }

  .headline {
    position: absolute; top: 300px; left: 10px; right: 10px;
    text-align: center;
    font-family: "Poppins", Arial, sans-serif;
    font-weight: 700; font-size: 14.8px; line-height: 21px;
    color: var(--blue);
  }
  .body-copy {
    position: absolute; top: 349px;
    text-align: center;
    font-size: 9.7px; line-height: 17px; color: var(--grey);
  }
  .screen--date .body-copy { left: 35px; right: 35px; }
  .screen--pickup .body-copy { left: 20px; right: 20px; }
  .screen--receive .body-copy { top: 330px; left: 24px; right: 24px; }

  .tour-button {
    position: absolute; top: 480px; left: 50%; transform: translateX(-50%);
    width: 103px; height: 30px; border-radius: 15px;
    background: var(--white);
    box-shadow: 0 3px 12px rgba(0, 84, 170, 0.16);
    border: none;
    font-family: "Roboto", Arial, sans-serif;
    font-weight: 500; font-size: 9.7px; letter-spacing: 0.2px;
    color: var(--blue);
  }
</style>
</head>
<body>

  <svg class="backdrop-wave" width="1200" height="803" viewBox="0 0 1200 803" aria-hidden="true">
    <path d="M0 0H1200V263Q600 583 0 263Z" fill="#0677BA"/>
  </svg>

  <section class="screen screen--date">
    <div class="status-bar">
      <span>12:00</span>
      <span class="status-icons">
        <svg width="11" height="7" viewBox="0 0 11 7"><rect x="0" y="4" width="2" height="3" fill="#1B1B1F"/><rect x="3" y="3" width="2" height="4" fill="#1B1B1F"/><rect x="6" y="1.5" width="2" height="5.5" fill="#1B1B1F"/><rect x="9" y="0" width="2" height="7" fill="#1B1B1F"/></svg>
        <svg width="16" height="8" viewBox="0 0 16 8"><rect x="0.5" y="0.5" width="13" height="7" rx="2" fill="none" stroke="#1B1B1F"/><rect x="2" y="2" width="10" height="4" rx="1" fill="#1B1B1F"/><rect x="14.5" y="2.5" width="1.5" height="3" fill="#1B1B1F"/></svg>
      </span>
    </div>
    <header class="app-header">
      <svg class="app-header__back" width="15" height="10" viewBox="0 0 15 10"><path d="M5 1 1 5l4 4M1 5h14" fill="none" stroke="#1B1B1F" stroke-width="1.6"/></svg>
      <h1 class="app-header__title">Date and Time</h1>
      <span class="app-header__menu"><svg width="10" height="8" viewBox="0 0 10 8"><path d="M0 1h10M0 4h10M0 7h10" stroke="#1B1B1F" stroke-width="1.3"/></svg></span>
    </header>
    <div class="illustration" role="img" aria-label="Laundry illustration: a person ticking pickup dates on a large blue calendar"></div>
    <h2 class="headline">Select a Convenient Pickup Date and Time.</h2>
    <p class="body-copy">We can collect from your home, office or wherever works for you.</p>
    <button class="tour-button">SKIP TOUR</button>
  </section>

  <section class="screen screen--pickup">
    <div class="status-bar">
      <span>12:00</span>
      <span class="status-icons">
        <svg width="11" height="7" viewBox="0 0 11 7"><rect x="0" y="4" width="2" height="3" fill="#1B1B1F"/><rect x="3" y="3" width="2" height="4" fill="#1B1B1F"/><rect x="6" y="1.5" width="2" height="5.5" fill="#1B1B1F"/><rect x="9" y="0" width="2" height="7" fill="#1B1B1F"/></svg>
        <svg width="16" height="8" viewBox="0 0 16 8"><rect x="0.5" y="0.5" width="13" height="7" rx="2" fill="none" stroke="#1B1B1F"/><rect x="2" y="2" width="10" height="4" rx="1" fill="#1B1B1F"/><rect x="14.5" y="2.5" width="1.5" height="3" fill="#1B1B1F"/></svg>
      </span>
    </div>
    <header class="app-header">
      <svg class="app-header__back" width="15" height="10" viewBox="0 0 15 10"><path d="M5 1 1 5l4 4M1 5h14" fill="none" stroke="#1B1B1F" stroke-width="1.6"/></svg>
      <h1 class="app-header__title">Pick Them Up</h1>
      <span class="app-header__menu"><svg width="10" height="8" viewBox="0 0 10 8"><path d="M0 1h10M0 4h10M0 7h10" stroke="#1B1B1F" stroke-width="1.3"/></svg></span>
    </header>
    <div class="illustration" role="img" aria-label="Laundry illustration: small workers loading baskets of clothes into large washing machines"></div>
    <h2 class="headline">Your Driver Will Come and Pick Them Up</h2>
    <p class="body-copy">Your items will then be processed according to the specifications you noted in the app.</p>
    <button class="tour-button">SKIP TOUR</button>
  </section>

  <section class="screen screen--receive">
    <div class="status-bar">
      <span>12:00</span>
      <span class="status-icons">
        <svg width="11" height="7" viewBox="0 0 11 7"><rect x="0" y="4" width="2" height="3" fill="#1B1B1F"/><rect x="3" y="3" width="2" height="4" fill="#1B1B1F"/><rect x="6" y="1.5" width="2" height="5.5" fill="#1B1B1F"/><rect x="9" y="0" width="2" height="7" fill="#1B1B1F"/></svg>
        <svg width="16" height="8" viewBox="0 0 16 8"><rect x="0.5" y="0.5" width="13" height="7" rx="2" fill="none" stroke="#1B1B1F"/><rect x="2" y="2" width="10" height="4" rx="1" fill="#1B1B1F"/><rect x="14.5" y="2.5" width="1.5" height="3" fill="#1B1B1F"/></svg>
      </span>
    </div>
    <header class="app-header">
      <svg class="app-header__back" width="15" height="10" viewBox="0 0 15 10"><path d="M5 1 1 5l4 4M1 5h14" fill="none" stroke="#1B1B1F" stroke-width="1.6"/></svg>
      <h1 class="app-header__title">Receive Your Items</h1>
      <span class="app-header__menu"><svg width="10" height="8" viewBox="0 0 10 8"><path d="M0 1h10M0 4h10M0 7h10" stroke="#1B1B1F" stroke-width="1.3"/></svg></span>
    </header>
    <div class="illustration" role="img" aria-label="Laundry illustration: a courier delivering a parcel of clean clothes beside blue location pins"></div>
    <h2 class="headline">Receive Your Clean Items</h2>
    <p class="body-copy">You'll be notified that your clothes are ready, Set up a delivery and clean,, fresh clothes will be on their way to your door.</p>
    <button class="tour-button">START</button>
  </section>

</body>
</html>
```